Double Gate Fold Brochure for Medical Center

We need an elegant design for a double-gate fold brochure for a medical center.
- Logo is attached
- Output must be in .AI format
- Brand colors is gold/light brown, as used in the logo
- The print template for 14"x 8.5" double-gate brochure is attached. (zip)
- Below is a link to content and images. Please be creative about the layouts, effect and placements.

https://slides.vornatek.net/deck/q/7Qv-2KmT_w9XrLp0aZc3HhE5nYbU4sJdFgMi1oRtS8y/open?mode=sharing

```html
<!DOCTYPE html>
<html lang="en">
<head>
<meta charset="utf-8">
<title>Halcyon Surgical Institute – Physician Brochure</title>
<link href="https://fonts.googleapis.com/css2?family=Titillium+Web:ital,wght@0,300;0,400;0,600;0,700;1,600&display=swap" rel="stylesheet">
<style>
:root{
  --gold:#b19b6b;
  --gold-text:#a88c55;
  --charcoal:#58585a;
  --ink:#4a4a4c;
  --white:#ffffff;
  --paper:#eeeeef;
  --tick:#b9a57a;
}
*{box-sizing:border-box;margin:0;padding:0}
html,body{width:1200px;height:796px;overflow:hidden;background:var(--paper)}
body{font-family:"Titillium Web",sans-serif;color:var(--ink)}
.brochure{
  position:absolute;left:10px;top:36px;width:1296px;height:795px;
  transform:scale(0.9105);transform-origin:0 0;
  background:var(--white);box-shadow:0 6px 18px rgba(0,0,0,.25);overflow:hidden;
}
.panel{position:absolute;top:0}
.panel--facility{left:0;width:330px;height:795px;background:var(--white)}
.panel--equipment{left:330px;width:318px;height:415px;background:var(--gold);color:var(--white)}
.panel--hospitality{left:648px;width:318px;height:415px;background:var(--charcoal);color:var(--white)}
.panel--advantage{left:966px;width:330px;height:795px;background:var(--white)}
.heading{position:absolute;font-weight:700;font-size:20px;letter-spacing:.3px;padding-left:15px;line-height:1;white-space:nowrap}
.heading::before{content:"";position:absolute;left:0;top:-1px;border-left:9px solid var(--gold);border-top:11px solid transparent;border-bottom:11px solid transparent}
.heading--gold{color:var(--gold-text)}
.heading--light{color:var(--white)}
.heading--light::before{border-left-color:var(--white)}
.panel--hospitality .heading::before{border-left-color:var(--gold)}
.copy{position:absolute;font-weight:300;font-size:15.3px;line-height:18.2px}
.ticks{position:absolute;list-style:none;font-weight:300;font-size:15.3px;line-height:18.2px}
.ticks li{position:relative;padding-left:18px}
.ticks li::before{content:"";position:absolute;left:0;top:5px;width:8px;height:8px;border:1px solid var(--tick)}
.ticks li::after{content:"";position:absolute;left:3px;top:4px;width:3px;height:7px;border:solid var(--tick);border-width:0 1.5px 1.5px 0;transform:rotate(40deg)}
.ticks--light li::before,.ticks--light li::after{border-color:rgba(255,255,255,.85)}
.photo{position:absolute}
.photo--reception{left:0;top:165px;width:330px;height:208px;background:linear-gradient(160deg,#c9b69a 0%,#ededeb 40%,#dfe2e4 100%);border-top:3px solid var(--gold);border-bottom:3px solid var(--gold)}
.photo--recovery{left:0;top:567px;width:330px;height:228px;background:linear-gradient(170deg,#f4f4f3 0%,#dcdfe1 60%,#b9bcbf 100%);border-top:8px solid var(--gold)}
.photo--theatre{left:330px;top:415px;width:636px;height:380px;background:linear-gradient(180deg,#d7dcdc 0%,#eef0ef 45%,#a9aeb0 100%);border-top:6px solid var(--gold)}
.contact{position:absolute;left:0;top:642px;width:330px;height:116px;background:var(--gold);color:var(--white);padding:9px 0 0 20px;font-size:15px;line-height:18.2px;font-weight:400;font-style:normal}
.contact__name{font-weight:600;font-style:italic}
.contact__gap{height:18px}
.photo--portrait{left:198px;top:622px;width:106px;height:133px;background:linear-gradient(180deg,#c6c8cb 0%,#8f9296 55%,#2f3338 100%);border:2px solid var(--white);border-radius:4px;box-shadow:0 1px 4px rgba(0,0,0,.3)}
</style>
</head>
<body>
<main class="brochure">

  <section class="panel panel--facility">
    <h2 class="heading heading--gold" style="left:34px;top:30px">FACILITY</h2>
    <p class="copy" style="left:34px;top:62px;width:282px">Established in 2017 and Accredited by NSAC, Halcyon Surgical Institute is strategically located in heart of South Bayat one of the most prestigious buildings in the area.</p>
    <div class="photo photo--reception" role="img" aria-label="Bright reception lobby with curved white desk and wood ceiling"></div>
    <h2 class="heading heading--gold" style="left:34px;top:394px;font-size:17px;font-weight:600">Our 14,000 sq ft. facility includes:</h2>
    <ul class="ticks" style="left:34px;top:425px;width:245px">
      <li>4 integrated operating rooms equipped with latest technology</li>
      <li>8 private recovery rooms with overnight stay</li>
      <li>Luxurious reception area</li>
      <li>Physician lounge &amp; pantry</li>
      <li>Spacious recreational outdoor patio</li>
    </ul>
    <div class="photo photo--recovery" role="img" aria-label="Recovery ward with hospital beds and curtains"></div>
  </section>

  <section class="panel panel--equipment">
    <h2 class="heading heading--light" style="left:20px;top:30px">EQUIPMENT</h2>
    <p class="copy" style="left:20px;top:61px;width:265px">We are proud to offer our physicians the latest in surgical technology:</p>
    <ul class="ticks ticks--light" style="left:20px;top:109px;width:296px">
      <li>Integrated laparoscopic equipment</li>
      <li>5K resolution camera head</li>
      <li>4K, 32" boom monitors</li>
      <li>Onsite radiology &amp; fluoroscopy</li>
      <li>Integrated endoscopy suite</li>
      <li>V-view video laryngoscope</li>
      <li>Fiberoptic laryngoscope</li>
      <li>ClearWave A6 Portable Ultrasound</li>
      <li>Advanced laparoscopic and<br>arthroscopic instruments</li>
      <li>Tidal Rover Suction/ Irrigation systems</li>
      <li>Central gas system</li>
      <li>Hospital grade beds in recovery rooms</li>
      <li>Fully implemented EMR</li>
      <li>Onsite dictation software</li>
    </ul>
  </section>

  <section class="panel panel--hospitality">
    <h2 class="heading heading--light" style="left:14px;top:30px">HOSPITALITY</h2>
    <ul class="ticks ticks--light" style="left:14px;top:63px;width:300px">
      <li>8 private recovery rooms equipped with<br>hospital grade beds and cable TV and apps</li>
      <li>Overnight and extended stay capability<br>for patient comfort</li>
      <li>24/7 support staff</li>
      <li>Transfer agreement with an advanced<br>closeby hospital</li>
      <li>Dedicated physician liaison</li>
      <li>Complimentary stay for physicians and<br>patients at the next-door Bayview hotel</li>
      <li>Courtesy transportations to/from facility<br>for surgeons and patients</li>
      <li>Free parking for physicians, staff,<br>patients and families.</li>
      <li>Walking distance to Harbor Point Fashion<br>Center, Hotels and Restaurants</li>
    </ul>
  </section>

  <div class="photo photo--theatre" role="img" aria-label="Operating room with surgical table, boom monitors and surgical lights"></div>

  <section class="panel panel--advantage">
    <h2 class="heading heading--gold" style="left:28px;top:30px">PHYSICIAN ADVANTAGE</h2>
    <p class="copy" style="left:28px;top:61px;width:290px">Halcyon is your facility of choice for:</p>
    <ul class="ticks" style="left:28px;top:92px;width:290px">
      <li>General Surgery</li><li>Bariatric Surgery</li><li>Gynecology</li><li>Urology</li>
      <li>Orthopedics</li><li>Spine Surgery</li><li>Pain management</li><li>Plastic &amp; Reconstructive</li>
      <li>Hand Surgery</li><li>Pediatric Surgery</li><li>Podiatric Surgery</li><li>Head and Neck Surgery</li>
      <li>ENT</li><li>Colon &amp; Rectal Surgery</li>
    </ul>
    <p class="copy" style="left:28px;top:371px;width:290px">Our “Physician Partnership Program” are<br>structured by one of the most respected<br>healthcare law firms in SoCal</p>
    <ul class="ticks" style="left:28px;top:450px;width:290px">
      <li>No Buy-In required</li><li>No Non-Compete Clause</li><li>No Long-Term Commitment</li>
      <li>Guaranteed Membership Status</li><li>No-membership fee</li>
    </ul>
    <p class="copy" style="left:28px;top:568px;width:290px">For more information about Physician<br>Partnership Programs, please contact:</p>
    <address class="contact">
      <div class="contact__name">Marcus Delavan, MBA</div>
      <div>Director of Operation</div>
      <div class="contact__gap"></div>
      <div>Tel: 310 555 0148</div>
      <div>marcus@halcyonsi.com</div>
    </address>
    <div class="photo photo--portrait" role="img" aria-label="Portrait of the director of operation"></div>
  </section>

</main>
</body>
</html>
```